Need simple and modern looking business card with all my information on one side and logo on the other side
Info :
Company name - VELMAR CONSTRUCTION LLC
Company addres- 418 harbor 87th. Dunmoor park ny 10352
Email- velmarllc@tridomail.Com
Company phone number 555-318-6094
Cell number- 555-742-0583
Web site - velmarllc.Com
My name Gerald tomasino

Target Market(s)

Construction , home improvement, remodeling

Industry/Entity Type

Construction

Contact Information for Business Card

It has to be moder but at the same time simple

Font styles to use
Sans Serif

Colors
0255a3
ffffff
000000
f78f20
b1b1b1
9d9d9d
1b1b1b
33a6d7
ec1f27

Requirements
Must have
• My logo on one side maybe with a some kind of background on the other side all my information
Nice to have
• Some kind of background pictures provided by you .PLEASE HAVE ACCOUNT WITH PIXELVAULT WILL NOT PAY ANY EXTRA FEES .
Should not have
• Any kind of hamer, nails,screws, helmets itp. Please do not copy the other designs come up with something new.

```html
<!DOCTYPE html>
<html lang="en">
<head>
<meta charset="utf-8">
<title>Velmar Construction LLC — Business Card</title>
<link href="https://fonts.googleapis.com/css2?family=Raleway:wght@500;600;800&display=swap" rel="stylesheet">
<style>
  :root {
    --card-dark: #231f20;
    --orange: #f78f20;
    --orange-light: #f9a825;
    --white: #ffffff;
    --backdrop-top: #a8905a;
    --backdrop-bottom: #94ae94;
  }
  * { box-sizing: border-box; margin: 0; padding: 0; }
  html, body { width: 1200px; height: 856px; overflow: hidden; }
  body {
    position: relative;
    background: linear-gradient(180deg, var(--backdrop-top), var(--backdrop-bottom));
    font-family: "Raleway", sans-serif;
  }
  .card {
    position: absolute;
    width: 560px; height: 320px;
    border-radius: 28px;
    background: var(--card-dark);
    overflow: hidden;
    box-shadow: 0 14px 30px rgba(0,0,0,0.35);
  }
  .card-front { left: 580px; top: 96px; }
  .card-back { left: 60px; top: 440px; }
  .swoosh { position: absolute; inset: 0; width: 100%; height: 100%; }

  .brand {
    position: absolute;
    display: flex; align-items: center; gap: 12px;
    color: var(--white);
    font-weight: 600;
  }
  .brand-mark { width: 18px; height: 18px; background: var(--orange); flex: none; }
  .brand-name { line-height: 1; letter-spacing: 0.06em; }
  .brand-name .line-main, .brand-name .line-sub { display: block; }

  .card-front .brand { right: 44px; bottom: 82px; }
  .card-front .line-main { font-size: 58px; }
  .card-front .line-sub { font-size: 19px; letter-spacing: 0.12em; margin-top: 4px; }

  .card-back .brand { right: 40px; top: 56px; }
  .card-back .brand-mark { width: 12px; height: 12px; }
  .card-back .line-main { font-size: 34px; }
  .card-back .line-sub { font-size: 11px; letter-spacing: 0.12em; margin-top: 3px; }

  .divider {
    position: absolute; left: 240px; right: 36px; top: 122px;
    height: 1px; background: var(--orange);
  }
  .holder-name {
    position: absolute; left: 230px; top: 134px;
    color: var(--orange);
    font-weight: 800; font-size: 24px; letter-spacing: 0.03em;
  }
  .name-rule {
    position: absolute; left: 230px; width: 230px; top: 168px;
    height: 1px; background: var(--orange);
  }
  .contact-list {
    position: absolute; left: 230px; top: 178px;
    list-style: none;
    color: var(--white); font-weight: 500; font-size: 16px;
  }
  .contact-list li { display: flex; align-items: center; gap: 10px; height: 24px; }
  .contact-icon { width: 16px; height: 16px; flex: none; }
  .address {
    position: absolute; left: 230px; top: 282px;
    color: var(--white); font-weight: 500; font-size: 15px;
  }
</style>
</head>
<body>

<svg width="0" height="0" style="position:absolute" aria-hidden="true">
  <defs>
    <linearGradient id="swoosh-fill" x1="0" y1="1" x2="1" y2="0">
      <stop offset="0" stop-color="#f78f20"/>
      <stop offset="1" stop-color="#f9a825"/>
    </linearGradient>
    <symbol id="swoosh-front" viewBox="0 0 560 320">
      <path d="M70 320 C130 180 300 50 560 0 L560 34 C340 56 180 170 138 320 Z" fill="url(#swoosh-fill)"/>
      <path d="M0 300 C70 200 170 120 300 70 C190 130 90 210 22 320 L0 320 Z" fill="url(#swoosh-fill)"/>
    </symbol>
    <symbol id="swoosh-back" viewBox="0 0 560 320">
      <path d="M60 320 C75 250 110 180 160 135 C240 65 400 20 560 0 L560 12 C400 28 250 80 190 150 C150 200 125 260 112 320 Z" fill="url(#swoosh-fill)"/>
      <path d="M0 296 C30 250 65 205 110 170 C75 210 40 260 18 320 L0 320 Z" fill="url(#swoosh-fill)"/>
    </symbol>
  </defs>
</svg>

<section class="card card-front" aria-label="Card front">
  <svg class="swoosh" aria-hidden="true"><use href="#swoosh-front"/></svg>
  <div class="brand">
    <span class="brand-mark"></span>
    <span class="brand-name">
      <span class="line-main">VELMAR</span>
      <span class="line-sub">CONSTRUCTION LLC</span>
    </span>
  </div>
</section>

<section class="card card-back" aria-label="Card back">
  <svg class="swoosh" aria-hidden="true"><use href="#swoosh-back"/></svg>
  <div class="brand">
    <span class="brand-mark"></span>
    <span class="brand-name">
      <span class="line-main">VELMAR</span>
      <span class="line-sub">CONSTRUCTION LLC</span>
    </span>
  </div>
  <div class="divider"></div>
  <h1 class="holder-name">GERALD TOMASINO</h1>
  <div class="name-rule"></div>
  <ul class="contact-list">
    <li>
      <svg class="contact-icon" viewBox="0 0 16 16" aria-hidden="true"><rect x="1.5" y="3.5" width="13" height="9" fill="none" stroke="#f78f20" stroke-width="1.3"/><path d="M1.5 3.5 L8 9 L14.5 3.5" fill="none" stroke="#f78f20" stroke-width="1.3"/></svg>
      velmarllc@tridomail.com
    </li>
    <li>
      <svg class="contact-icon" viewBox="0 0 16 16" aria-hidden="true"><circle cx="8" cy="8" r="7" fill="none" stroke="#f78f20" stroke-width="1.3"/><path d="M5.2 4.6 L6.6 4.4 L7.2 6.2 L6.3 6.9 C6.8 8 7.8 9 8.9 9.6 L9.6 8.7 L11.4 9.3 L11.2 10.8 C8 11 5 8 5.2 4.6 Z" fill="#f78f20"/></svg>
      555-318-6094
    </li>
    <li>
      <svg class="contact-icon" viewBox="0 0 16 16" aria-hidden="true"><circle cx="8" cy="8" r="7" fill="none" stroke="#f78f20" stroke-width="1.3"/><rect x="5.6" y="3.8" width="4.8" height="8.4" rx="1" fill="none" stroke="#f78f20" stroke-width="1.2"/><circle cx="8" cy="10.8" r="0.6" fill="#f78f20"/></svg>
      555-742-0583
    </li>
    <li>
      <svg class="contact-icon" viewBox="0 0 16 16" aria-hidden="true"><circle cx="8" cy="8" r="7" fill="#f78f20"/><ellipse cx="8" cy="8" rx="3" ry="7" fill="none" stroke="#231f20" stroke-width="1"/><path d="M1 8 H15 M2.5 4.5 H13.5 M2.5 11.5 H13.5" stroke="#231f20" stroke-width="1"/></svg>
      www.velmarllc.com
    </li>
  </ul>
  <p class="address">418 Harbor 87th. Dunmoor Park, NY 10352</p>
</section>

</body>
</html>
```